New Company Business Card design

Looking for a corporate looking business card utilising my new logo design - the logo i would like embossed as one option and flat as another - simplistic but stylish - less is more - we are an import export business launching into the market - i would like a couple of options as main background - Grey or Black

```html
<!DOCTYPE html>
<html lang="en">
<head>
<meta charset="utf-8">
<title>Meridian Trade Partners – Business Card</title>
<link rel="stylesheet" href="https://fonts.googleapis.com/css2?family=Work+Sans:wght@400;500&display=swap">
<style>
  :root {
    --backdrop: #2b2b2d;
    --card: #1b1b1d;
    --brand-blue: #1479c4;
    --text-light: #f2f2f2;
    --text-muted: #b9b9bb;
  }
  * { margin: 0; padding: 0; box-sizing: border-box; }
  html, body { width: 1200px; height: 900px; overflow: hidden; }
  body {
    background: var(--backdrop);
    font-family: "Work Sans", Arial, sans-serif;
    position: relative;
  }
  .card {
    position: absolute;
    width: 620px;
    height: 350px;
    background: var(--card);
    border-radius: 3px;
    box-shadow: 0 14px 30px rgba(0,0,0,0.45);
  }
  .card--front { left: 330px; top: 70px; }
  .card--back { left: 250px; top: 470px; }

  .brand {
    display: flex;
    align-items: center;
    gap: 14px;
    color: var(--brand-blue);
    font-weight: 500;
    text-transform: uppercase;
    letter-spacing: 3px;
    white-space: nowrap;
  }
  .brand__dot {
    width: 16px; height: 16px;
    border-radius: 50%;
    background: var(--brand-blue);
    flex: none;
  }
  .card--front .brand {
    position: absolute;
    left: 0; right: 0; top: 150px;
    justify-content: center;
    font-size: 30px;
  }

  .contact-block {
    position: absolute;
    right: 48px;
    top: 40px;
    text-align: right;
  }
  .contact-block .brand {
    justify-content: flex-end;
    font-size: 20px;
    letter-spacing: 2px;
  }
  .brand__dot--small { width: 12px; height: 12px; }
  .tagline {
    margin-top: 8px;
    font-size: 9px;
    letter-spacing: 3px;
    color: var(--text-muted);
    text-transform: uppercase;
    white-space: nowrap;
  }
  .person-name {
    margin-top: 22px;
    font-size: 28px;
    font-weight: 500;
    color: var(--brand-blue);
    text-transform: uppercase;
    line-height: 1;
  }
  .person-role {
    margin-top: 6px;
    font-size: 18px;
    color: var(--text-light);
  }
  .address {
    margin-top: 12px;
    font-size: 17px;
    line-height: 1.3;
    color: var(--text-light);
    font-style: normal;
  }
  .contact-list {
    list-style: none;
    margin-top: 10px;
    font-size: 17px;
    color: var(--text-light);
  }
  .contact-list li {
    display: flex;
    justify-content: flex-end;
    align-items: center;
    gap: 10px;
    line-height: 1.4;
  }
  .contact-list svg { width: 14px; height: 14px; flex: none; }
</style>
</head>
<body>

  <section class="card card--front" aria-label="Business card front">
    <div class="brand"><span class="brand__dot"></span>Meridian Trade Partners</div>
  </section>

  <section class="card card--back" aria-label="Business card back">
    <div class="contact-block">
      <div class="brand"><span class="brand__dot brand__dot--small"></span>Meridian Trade Partners</div>
      <p class="tagline">Worldwide supply for every local market</p>
      <p class="person-name">Daniel Reyes</p>
      <p class="person-role">Director</p>
      <address class="address">820 Harbor View Dr<br>Linden, CA 95236-4410</address>
      <ul class="contact-list">
        <li>555-214-7730
          <svg viewBox="0 0 16 16" fill="none" stroke="#f2f2f2" stroke-width="1.4"><path d="M4 1.5h2.5l1 3.5-1.6 1.2a8 8 0 0 0 3.9 3.9L11 8.5l3.5 1V12a2 2 0 0 1-2 2A10.5 10.5 0 0 1 2 3.5a2 2 0 0 1 2-2z"/></svg>
        </li>
        <li>hello@meridiantrade.com
          <svg viewBox="0 0 16 16" fill="none" stroke="#f2f2f2" stroke-width="1.4"><rect x="1.5" y="3.5" width="13" height="9"/><path d="M1.5 3.5 8 9l6.5-5.5"/></svg>
        </li>
        <li>www.meridiantrade.com
          <svg viewBox="0 0 16 16" fill="none" stroke="#f2f2f2" stroke-width="1.2"><circle cx="8" cy="8" r="6.5"/><ellipse cx="8" cy="8" rx="3" ry="6.5"/><path d="M1.5 8h13M2.5 5h11M2.5 11h11"/></svg>
        </li>
      </ul>
    </div>
  </section>

</body>
</html>
```